Edible Insect Sticker packaging design

The successful designer for this product will be hired again for more packaging design products in this product range.
We are a company that manufactures edible insects and we have some new products coming out we ned packaging for. As you can imagine the stickers are very small 50mm x 50mm.
Each sticker design will be in a set  of 2 (one for the front and one for the back of the packaging).
The front will contain the weight of the product (in grams) as well as the name of the product and design.
The back will contain our company logo and info as well as NIP (Nutritional Information Panel), ingredient declaration, and 3-4 lines of information about how edible insects are great for the environment.
At this stage I would like the packaging to have a slightly environmental free, but still colourful and eye catching. I am open to any suggestions for the design though if you have some great ideas!
Must also contain the slogan (on front or back), "Are you Brave Enough?"
There are several products in the range, and would like the labels to be in a set. Basic lay out will be the same for each product, and the front sticker will be slightly different.
Products are
Zib-A-Lop Tundle- a fly shaped chocolate that contains coconut and fly pupae
Plinky Pebbles- 5 x roasted crickets
Tootle Twirlies- 5 x roasted mealworms
Fudge Dipped Fidgets- 5 x insects, chocolate coated in milk, white or dark chocolate. Insects include crickets, mealworms and fly pupae
Specific information (eg, NIP, ingredients etc) will be sent to chosen designer to add to the deisgn.
Attached is image of 3 products (Zib-A-Lop Tundle, roasted mealworms and roasted crickets) as well as logo. The chocolate coated bugs are the 2 types of roasted bugs pictured in the attachment coated in chocolate.

Updates
Design can be square or round 

Reason: Several designers have asked for an extension to submit new/ revised designs.

Reason: I have extended the deadline by one day to allow for revisions and new designs to be submitted.

```html
<!DOCTYPE html>
<html lang="en">
<head>
<meta charset="utf-8">
<title>Edible Insect Sticker Set</title>
<link rel="stylesheet" href="https://fonts.googleapis.com/css2?family=Chewy&family=Caveat+Brush&family=Arimo:wght@400;700&display=swap">
<style>
  :root{
    --bg-top:#0f110d;
    --bg-mid:#1c2019;
    --hanger:#d9d9d7;
    --hanger-slot:#101010;
    --slogan-red:#e0262b;
    --white:#ffffff;
    --ink:#2a1a10;
    --back-dark:#2c2017;
    --green:#8cc63f;
    --green-light:#c8e27a;
    --yellow:#e8e23a;
    --yellow-light:#f4ef8a;
    --orange:#f39a1e;
    --orange-light:#fbcb57;
    --rust:#ee7a22;
    --logo-olive:#7b8c36;
    --weight-grey:#6f7b5c;
    --weight-orange:#ef7a25;
    --weight-ochre:#ea8a1c;
  }
  *{box-sizing:border-box;margin:0;padding:0}
  html,body{width:1200px;height:871px;overflow:hidden}
  body{
    background:radial-gradient(ellipse at 50% 45%,var(--bg-mid) 0%,var(--bg-top) 75%);
    font-family:"Arimo",Arial,sans-serif;
    position:relative;
  }
  .sticker-set{position:absolute;top:98px;width:261px}
  .sticker-set--zib{left:117px}
  .sticker-set--plinky{left:473px}
  .sticker-set--tootle{left:841px}

  .hanger{height:129px;background:var(--hanger);position:relative}
  .hanger__slot{position:absolute;left:78px;top:36px;width:105px;height:22px;border-radius:11px;background:var(--hanger-slot)}
  .hanger__slot::before{content:"";position:absolute;left:35px;top:-10px;width:35px;height:20px;border-radius:12px 12px 0 0;background:var(--hanger-slot)}

  .front{position:relative;height:262px;overflow:hidden;background:var(--front-base)}
  .front__art{position:absolute;inset:0}
  .front__slogan{
    position:absolute;left:6px;top:70px;width:112px;height:112px;border-radius:50%;
    background:var(--slogan-red);color:var(--white);
    font-family:"Chewy",cursive;font-size:21px;line-height:20px;
    display:flex;align-items:center;justify-content:center;text-align:center;
    border:2px solid var(--white);
  }
  .front__name{
    position:absolute;left:6px;top:158px;width:270px;
    font-family:"Caveat Brush",cursive;font-size:36px;color:var(--name-fill);
    -webkit-text-stroke:1.4px var(--ink);
    transform:rotate(-7deg);white-space:nowrap;letter-spacing:-.5px;
  }
  .front__weight{
    position:absolute;left:112px;top:212px;width:66px;height:66px;border-radius:50%;
    background:var(--weight);color:var(--white);
    font-family:"Chewy",cursive;font-size:25px;text-align:center;padding-top:13px;
  }

  .gap{height:42px}

  .back{height:265px}
  .back__brand{height:117px;background:var(--white);position:relative}
  .brand-name{
    position:absolute;left:22px;top:28px;width:150px;
    font-family:"Chewy",cursive;font-size:29px;line-height:28px;color:var(--logo-olive);text-align:center;
  }
  .brand-mark{position:absolute;left:186px;top:30px;width:40px;height:40px;border-radius:50%;background:var(--logo-olive)}
  .back__info{height:148px;background:var(--back-dark);padding:10px 10px 0}
  .info-panel{
    height:128px;border-radius:9px;background:var(--panel);position:relative;
    border:1px solid rgba(255,255,255,.6);padding:8px 8px 0;color:var(--ink);
  }
  .info-panel__row{display:flex;gap:6px}
  .nip{width:118px}
  .nip__title{font-size:7.5px;font-weight:700;border-bottom:1px solid var(--ink);line-height:10px}
  .nip__box{background:var(--white);margin-top:2px;padding:2px 3px;font-size:5px;line-height:7px}
  .nip__box .rule{border-top:2px solid var(--ink);margin:1px 0}
  .nip__box .line{display:flex;justify-content:space-between;border-top:.5px solid #999}
  .eco{flex:1;font-size:5.4px;line-height:7px}
  .eco__title{font-size:5px;font-weight:700;margin-bottom:8px}
  .eco__text{padding:0 8px;text-align:center}
  .ingredients{margin-top:6px;font-size:7.5px;font-weight:700;border-bottom:1px solid var(--ink);width:118px}
  .ingredients__box{margin-top:3px;height:10px;width:118px;border:1px solid var(--white);border-radius:2px}

  .theme--zib{--front-base:var(--green);--name-fill:var(--green-light);--weight:var(--weight-grey);--panel:var(--rust)}
  .theme--plinky{--front-base:var(--yellow);--name-fill:var(--yellow-light);--weight:var(--weight-orange);--panel:var(--green)}
  .theme--tootle{--front-base:var(--orange);--name-fill:var(--orange-light);--weight:var(--weight-ochre);--panel:var(--orange-light)}
</style>
</head>
<body>

<section class="sticker-set sticker-set--zib theme--zib">
  <div class="hanger"><span class="hanger__slot"></span></div>
  <div class="front">
    <svg class="front__art" viewBox="0 0 261 262" width="261" height="262">
      <defs><linearGradient id="artZib" x1="0" y1="0" x2="1" y2="1"><stop offset="0" stop-color="#3a2417"/><stop offset="1" stop-color="#c2631f"/></linearGradient></defs>
      <polygon points="0,0 261,0 261,150 0,205" fill="#ffffff"/>
      <polygon points="0,0 110,0 70,120 0,150" fill="#8cc63f"/>
      <polygon points="100,0 261,0 261,130 150,120 90,90" fill="url(#artZib)" role="img" aria-label="Illustration of a chocolate fly-shaped treat"/>
      <polygon points="0,205 261,150 261,262 0,262" fill="#8cc63f"/>
      <polygon points="0,235 261,180 261,200 0,255" fill="#c8e27a" opacity=".6"/>
    </svg>
    <div class="front__slogan">Are You<br>Brave<br>Enough<br>?</div>
    <div class="front__name">Zib-A-Lop Tundle</div>
    <div class="front__weight">10g</div>
  </div>
  <div class="gap"></div>
  <div class="back">
    <div class="back__brand"><div class="brand-name">KETTLE HOP PANTRY</div><span class="brand-mark"></span></div>
    <div class="back__info">
      <div class="info-panel">
        <div class="info-panel__row">
          <div class="nip">
            <div class="nip__title">NUTRITIONAL INFORMATION</div>
            <div class="nip__box">
              <div>Serving Size 10g</div><div>Serving Per Container 1</div><div class="rule"></div>
              <div><b>Amount Per Serving</b></div>
              <div class="line"><b>Calories 175</b><span>Calories from Fat 0</span></div>
              <div class="line"><span></span><b>% Daily Value*</b></div>
              <div class="line"><b>Total Fat 0g</b><span>0%</span></div>
              <div class="line"><span>Saturated Fat 0g</span><span>0%</span></div>
              <div class="line"><span>Trans Fat 0g</span><span></span></div>
            </div>
          </div>
          <div class="eco">
            <div class="eco__title">Information about how edible insects</div>
            <p class="eco__text">Insects need little water, land and feed. Farming them makes far less greenhouse gas than cattle.</p>
          </div>
        </div>
        <div class="ingredients">INGREDIENTS :</div>
        <div class="ingredients__box"></div>
      </div>
    </div>
  </div>
</section>

<section class="sticker-set sticker-set--plinky theme--plinky">
  <div class="hanger"><span class="hanger__slot"></span></div>
  <div class="front">
    <svg class="front__art" viewBox="0 0 261 262" width="261" height="262">
      <defs><linearGradient id="artPlinky" x1="0" y1="0" x2="1" y2="1"><stop offset="0" stop-color="#f6a23a"/><stop offset="1" stop-color="#c96a1c"/></linearGradient></defs>
      <polygon points="0,0 261,0 261,170 0,215" fill="#ffffff"/>
      <polygon points="0,0 40,0 0,60" fill="#b8d86a"/>
      <polygon points="70,0 261,0 261,120 190,150 120,110" fill="url(#artPlinky)" role="img" aria-label="Illustration of roasted cricket legs"/>
      <polygon points="0,215 261,170 261,262 0,262" fill="#e8e23a"/>
      <polygon points="0,262 261,225 261,262" fill="#f39a1e" opacity=".7"/>
    </svg>
    <div class="front__slogan">Are You<br>Brave<br>Enough<br>?</div>
    <div class="front__name">Plinky Pebbles</div>
    <div class="front__weight">10g</div>
  </div>
  <div class="gap"></div>
  <div class="back">
    <div class="back__brand"><div class="brand-name">KETTLE HOP PANTRY</div><span class="brand-mark"></span></div>
    <div class="back__info">
      <div class="info-panel">
        <div class="info-panel__row">
          <div class="nip">
            <div class="nip__title">NUTRITIONAL INFORMATION</div>
            <div class="nip__box">
              <div>Serving Size 10g</div><div>Serving Per Container 1</div><div class="rule"></div>
              <div><b>Amount Per Serving</b></div>
              <div class="line"><b>Calories 175</b><span>Calories from Fat 0</span></div>
              <div class="line"><span></span><b>% Daily Value*</b></div>
              <div class="line"><b>Total Fat 0g</b><span>0%</span></div>
              <div class="line"><span>Saturated Fat 0g</span><span>0%</span></div>
              <div class="line"><span>Trans Fat 0g</span><span></span></div>
            </div>
          </div>
          <div class="eco">
            <div class="eco__title">Information about how edible insects</div>
            <p class="eco__text">Insects need little water, land and feed. Farming them makes far less greenhouse gas than cattle.</p>
          </div>
        </div>
        <div class="ingredients">INGREDIENTS :</div>
        <div class="ingredients__box"></div>
      </div>
    </div>
  </div>
</section>

<section class="sticker-set sticker-set--tootle theme--tootle">
  <div class="hanger"><span class="hanger__slot"></span></div>
  <div class="front">
    <svg class="front__art" viewBox="0 0 261 262" width="261" height="262">
      <defs><linearGradient id="artTootle" x1="0" y1="0" x2="1" y2="1"><stop offset="0" stop-color="#f0a23a"/><stop offset="1" stop-color="#b5561a"/></linearGradient></defs>
      <polygon points="0,0 261,0 261,175 0,230" fill="#ffffff"/>
      <polygon points="80,0 261,0 261,110 180,130 110,60" fill="url(#artTootle)" role="img" aria-label="Illustration of a roasted mealworm"/>
      <polygon points="0,230 261,175 261,262 0,262" fill="#f39a1e"/>
      <polygon points="0,262 261,215 261,262" fill="#fbcb57" opacity=".6"/>
    </svg>
    <div class="front__slogan">Are You<br>Brave<br>Enough<br>?</div>
    <div class="front__name">Tootle Twirlies</div>
    <div class="front__weight">10g</div>
  </div>
  <div class="gap"></div>
  <div class="back">
    <div class="back__brand"><div class="brand-name">KETTLE HOP PANTRY</div><span class="brand-mark"></span></div>
    <div class="back__info">
      <div class="info-panel">
        <div class="info-panel__row">
          <div class="nip">
            <div class="nip__title">NUTRITIONAL INFORMATION</div>
            <div class="nip__box">
              <div>Serving Size 10g</div><div>Serving Per Container 1</div><div class="rule"></div>
              <div><b>Amount Per Serving</b></div>
              <div class="line"><b>Calories 175</b><span>Calories from Fat 0</span></div>
              <div class="line"><span></span><b>% Daily Value*</b></div>
              <div class="line"><b>Total Fat 0g</b><span>0%</span></div>
              <div class="line"><span>Saturated Fat 0g</span><span>0%</span></div>
              <div class="line"><span>Trans Fat 0g</span><span></span></div>
            </div>
          </div>
          <div class="eco">
            <div class="eco__title">Information about how edible insects</div>
            <p class="eco__text">Insects need little water, land and feed. Farming them makes far less greenhouse gas than cattle.</p>
          </div>
        </div>
        <div class="ingredients">INGREDIENTS :</div>
        <div class="ingredients__box"></div>
      </div>
    </div>
  </div>
</section>

</body>
</html>
```